Bref créative
Business Card design for Property Management Company
Harborlight Stewards
Professional
Corwin Talbot
P.O. Box K-4183
Nassau, Bahamas
corwin@harborlightstewardsgroup.com

```html
<!DOCTYPE html>
<html lang="en">
<head>
<meta charset="utf-8">
<title>Harborlight Stewards — Stationery</title>
<link href="https://fonts.googleapis.com/css2?family=Cinzel:wght@400;600&family=Open+Sans:wght@400;600&display=swap" rel="stylesheet">
<style>
:root{
  --bg:#eef0f2;
  --paper:#ffffff;
  --blue:#1f6199;
  --navy:#0f3b66;
  --ink:#1b1b1b;
  --muted:#6b7480;
}
*{box-sizing:border-box;margin:0;padding:0}
html,body{width:1200px;height:936px;overflow:hidden;background:var(--bg)}
body{position:relative;font-family:"Open Sans",sans-serif;color:var(--ink)}
.sheet{position:absolute;background:var(--paper);overflow:hidden;border:1px solid #dfe3e7}
.brand{position:absolute;display:flex;align-items:center;gap:8px}
.brand-dot{border-radius:50%;background:var(--blue);flex:none}
.brand-name{font-family:"Cinzel",serif;font-weight:600;color:var(--navy);line-height:1.05;white-space:nowrap}
.wave{position:absolute;left:0;bottom:0;width:100%}
.site{position:absolute;left:0;width:100%;text-align:center;font-family:"Cinzel",serif;color:#fff;letter-spacing:.5px;white-space:nowrap}
.contact{position:absolute;font-size:6px;line-height:1.55;color:var(--muted);white-space:nowrap}

/* letterhead */
.letterhead{left:183px;top:69px;width:389px;height:543px}
.letterhead .brand{left:28px;top:30px}
.letterhead .brand-dot{width:24px;height:24px}
.letterhead .brand-name{font-size:10px}
.letterhead .contact{left:218px;top:30px}
.watermark{position:absolute;left:148px;top:160px;width:94px;height:94px;border-radius:50%;background:var(--blue);opacity:.08}
.letterhead .site{bottom:14px;font-size:8px}

/* folder */
.folder{left:635px;top:43px;width:465px;height:574px}
.folder .brand{left:58px;top:254px;gap:14px}
.folder .brand-dot{width:60px;height:60px}
.folder .brand-name{font-size:26px}
.folder .site{bottom:16px;font-size:9px}

/* business cards */
.card-front{left:43px;top:668px;width:190px;height:102px}
.card-front .brand{left:12px;top:14px;gap:5px}
.card-front .brand-dot{width:14px;height:14px}
.card-front .brand-name{font-size:7px}
.card-front .contact{left:92px;top:14px;font-size:4.6px}
.card-front .contact b{color:var(--ink);font-weight:600;font-size:5.5px}
.card-back{left:43px;top:802px;width:190px;height:102px;background:var(--blue);border:none}
.card-back .brand{left:0;top:0;width:100%;height:100%;justify-content:center;flex-direction:column;gap:8px}
.card-back .brand-dot{width:30px;height:30px;background:#fff}
.card-back .brand-name{font-size:8px;color:#fff}

/* envelopes */
.envelope{left:267px;top:673px;width:432px;height:208px}
.envelope .brand{left:16px;top:18px;gap:8px}
.envelope .brand-dot{width:24px;height:24px}
.envelope .brand-name{font-size:10px}
.tagline{position:absolute;left:48px;top:48px;font-size:5.5px;color:var(--muted)}
.envelope-back{left:737px;top:673px;width:437px;height:208px}
.envelope-back svg{position:absolute;left:0;top:0;width:100%;height:100%}
.envelope-back .site{top:16px;font-size:9px}
</style>
</head>
<body>

<section class="sheet letterhead" aria-label="Letterhead">
  <div class="brand"><span class="brand-dot"></span><span class="brand-name">Harborlight<br>Stewards</span></div>
  <div class="contact">P.O. Box K-4183<br>Nassau, Bahamas<br>Tel 242-555-0147<br>Fax 242-555-0148<br>corwin@harborlightstewardsgroup.com</div>
  <div class="watermark"></div>
  <svg class="wave" viewBox="0 0 390 64" height="64" preserveAspectRatio="none">
    <path d="M0 30 C120 8 260 8 390 22 L390 64 L0 64Z" fill="var(--blue)"/>
    <path d="M0 26 C120 2 260 0 390 12 L390 20 C260 10 120 12 0 32Z" fill="var(--ink)"/>
    <path d="M0 38 C130 20 260 22 390 32 L390 36 C260 26 130 26 0 42Z" fill="#fff" opacity=".9"/>
  </svg>
  <div class="site">www.harborlightstewardsgroup.com</div>
</section>

<section class="sheet folder" aria-label="Presentation folder">
  <div class="brand"><span class="brand-dot"></span><span class="brand-name">Harborlight<br>Stewards</span></div>
  <svg class="wave" viewBox="0 0 460 70" height="70" preserveAspectRatio="none">
    <path d="M0 32 C140 8 300 8 460 22 L460 70 L0 70Z" fill="var(--blue)"/>
    <path d="M0 28 C140 2 300 0 460 12 L460 20 C300 10 140 12 0 34Z" fill="var(--ink)"/>
    <path d="M0 40 C150 22 300 24 460 34 L460 38 C300 28 150 28 0 44Z" fill="#fff" opacity=".9"/>
  </svg>
  <div class="site">www.harborlightstewardsgroup.com</div>
</section>

<section class="sheet card-front" aria-label="Business card front">
  <div class="brand"><span class="brand-dot"></span><span class="brand-name">Harborlight<br>Stewards</span></div>
  <div class="contact"><b>Corwin Talbot</b><br>Managing Director<br>P.O. Box K-4183<br>Nassau, Bahamas<br>Tel 242-555-0147<br>corwin@harborlightstewardsgroup.com</div>
</section>

<section class="sheet card-back" aria-label="Business card back">
  <div class="brand"><span class="brand-dot"></span><span class="brand-name">Harborlight Stewards</span></div>
</section>

<section class="sheet envelope" aria-label="Envelope front">
  <div class="brand"><span class="brand-dot"></span><span class="brand-name">Harborlight<br>Stewards</span></div>
  <div class="tagline">Trusted Property Care</div>
</section>

<section class="sheet envelope-back" aria-label="Envelope back">
  <svg viewBox="0 0 437 208" preserveAspectRatio="none">
    <path d="M0 0 H437 V46 C320 66 117 66 0 46Z" fill="var(--blue)"/>
    <path d="M0 46 C117 66 320 66 437 46" fill="none" stroke="#0b2f52" stroke-width="1"/>
  </svg>
  <div class="site">www.harborlightstewardsgroup.com</div>
</section>

</body>
</html>
```